Wedding Guestbook/Questionnaire Pages

I am looking for questionnaire-style guest book pages for a friend's wedding. The bride wants her guests to fill out a page of reflections on the couple and the wedding in lieu of a traditional guest book. The pages would be printed on 12x12 paper and bound in a book after the wedding.

I've attached a photo of the style of the pages as well as several documents that show colors and give a feel for the wedding.

I understand that this isn't a common project so I welcome any questions and would be more than happy to clarify things.

Thank you!

Target Market(s)

The bride and groom are a young couple and the wedding is more fun and whimisical than formal. The colors are primarily purple with green and silver accents.

Industry/Entity Type

Wedding

Requirements
Must have
• I would like to have 2 pages that are similar, but have different questions on them so that every guest doesn't answer the same questions. On each page it needs to say 'Mara & Declan,' 'May 27th, 2011,' and a place that says 'Guest Names' for the guest sign their names.
Nice to have
• Some of the questions we like are:
Do you have any advice or wishes for the bride and groom?
How far did you travel to get here?
How do you know Mara and Declan?
What’s your favorite memory with the bride and groom?
What has been your favorite part of the wedding?
What do you think they'll name their children?
Should not have
• The pages do not need to be extremely colorful. An ivory or white background with accents of color would be preferred.

```html
<!DOCTYPE html>
<html lang="en">
<head>
<meta charset="UTF-8">
<title>Mara &amp; Declan – Guest Page</title>
<link rel="stylesheet" href="https://fonts.googleapis.com/css2?family=Parisienne&family=Cormorant+Garamond:ital,wght@1,600&family=Arimo:wght@400;700&display=swap">
<style>
  :root {
    --purple: #622f78;
    --purple-text: #5c2d74;
    --green: #92d050;
    --rule: #cdc6e2;
    --ink: #111111;
    --paper: #ffffff;
    --petal-light: #c9c4f2;
    --petal-mid: #8f88e4;
    --petal-deep: #5a56c8;
  }
  * { margin: 0; padding: 0; box-sizing: border-box; }
  html, body {
    width: 1188px; height: 1200px; overflow: hidden;
    background: var(--paper);
  }
  .page {
    position: relative; width: 1188px; height: 1200px;
    background: var(--paper);
    font-family: "Arimo", Arial, sans-serif;
    color: var(--ink);
  }
  .stripes, .floral-crown, .floral-garland { position: absolute; left: 0; top: 0; }
  .monogram {
    position: absolute; left: 10px; top: 221px;
    width: 296px; height: 296px; border-radius: 50%;
    background: var(--purple);
    color: #fff;
    font-family: "Parisienne", cursive;
    overflow: hidden;
  }
  .monogram .first {
    position: absolute; left: 22px; top: 62px;
    font-size: 62px; line-height: 1;
  }
  .monogram .second {
    position: absolute; left: 48px; top: 132px;
    font-size: 48px; line-height: 1; white-space: nowrap;
  }
  .date {
    position: absolute; left: 176px; top: 701px;
    transform: translate(-50%, -50%) rotate(-90deg);
    font-size: 42px; color: var(--purple-text);
    white-space: nowrap; letter-spacing: 0.5px;
  }
  .guest-name {
    position: absolute; left: 0; top: 1086px; width: 193px;
    border-top: 1px solid #222;
  }
  .guest-name span {
    position: absolute; left: 28px; top: 14px; font-size: 18px;
  }
  .welcome {
    position: absolute; left: 346px; width: 758px; top: 140px;
    text-align: center; color: var(--purple-text);
    font-family: "Cormorant Garamond", serif; font-style: italic; font-weight: 600;
  }
  .welcome .title { font-size: 64px; line-height: 1; }
  .welcome .subtitle { font-size: 37px; line-height: 1; margin-top: 2px; }
  .section-band {
    position: absolute; left: 377px; top: 262px;
    width: 703px; height: 41px;
    background: var(--green); color: #fff;
    font-weight: 700; font-size: 22px; letter-spacing: 8.2px;
    display: flex; align-items: center; justify-content: center;
  }
  .questions { position: absolute; left: 379px; top: 0; width: 701px; list-style: none; }
  .question {
    position: absolute; left: 0; width: 701px; height: 101px;
    border-bottom: 1.5px solid var(--rule);
  }
  .question p {
    position: absolute; left: 2px; top: 20px;
    font-size: 21px; white-space: nowrap;
  }
</style>
</head>
<body>
<main class="page">

  <svg class="stripes" width="320" height="1200" viewBox="0 0 320 1200" aria-hidden="true">
    <rect x="214" y="190" width="7" height="920" fill="var(--green)"/>
    <line x1="234" y1="150" x2="234" y2="1110" stroke="var(--green)" stroke-width="4" stroke-dasharray="5 3"/>
    <rect x="248" y="101" width="8" height="1009" fill="var(--green)"/>
    <rect x="268" y="72" width="5" height="1038" fill="var(--green)"/>
    <rect x="285" y="43" width="13" height="1067" fill="var(--green)"/>
  </svg>

  <div class="monogram">
    <span class="first">Mara</span>
    <span class="second">&amp; Declan</span>
  </div>

  <div class="date">May 27th, 2011</div>

  <div class="guest-name"><span>Guest Name</span></div>

  <svg class="floral-crown" width="1188" height="210" viewBox="0 0 1188 210" role="img" aria-label="Border of blue and violet hydrangea blossoms across the top">
    <defs>
      <radialGradient id="petals" cx="50%" cy="40%" r="70%">
        <stop offset="0" stop-color="var(--petal-light)"/>
        <stop offset="0.6" stop-color="var(--petal-mid)"/>
        <stop offset="1" stop-color="var(--petal-deep)"/>
      </radialGradient>
    </defs>
    <path d="M350 40 Q350 8 390 8 L1060 8 Q1104 8 1104 44 L1104 170 Q1104 202 1070 202 L1010 202 Q990 202 990 178 L990 120 Q960 112 900 108 L560 108 Q500 112 488 124 L488 176 Q486 202 456 202 L380 202 Q350 202 350 172 Z" fill="url(#petals)" opacity="0.75"/>
  </svg>

  <header class="welcome">
    <div class="title">Welcome</div>
    <div class="subtitle">to M+D Wedding Page</div>
  </header>

  <div class="section-band">COMMENTS AND SUGGESTIONS</div>

  <ol class="questions">
    <li class="question" style="top:335px"><p>Do you have any advice or wishes for the bride and groom?</p></li>
    <li class="question" style="top:436px"><p>How far did you travel to get here?</p></li>
    <li class="question" style="top:537px"><p>How do you know Mara and Declan?</p></li>
    <li class="question" style="top:637px"><p>What’s your favorite memory with the bride and groom?</p></li>
    <li class="question" style="top:738px"><p>What do you think the bride and groom's first fight will be about?</p></li>
    <li class="question" style="top:839px"><p>What has been your favorite part of the wedding?</p></li>
    <li class="question" style="top:940px"><p>What do you think they'll name their children?</p></li>
  </ol>

  <svg class="floral-garland" width="1188" height="1200" viewBox="0 0 1188 1200" role="img" aria-label="Garland of small blue and violet hydrangea blossoms">
    <defs>
      <radialGradient id="garland-petals" cx="50%" cy="40%" r="70%">
        <stop offset="0" stop-color="var(--petal-light)"/>
        <stop offset="0.65" stop-color="var(--petal-mid)"/>
        <stop offset="1" stop-color="var(--petal-deep)"/>
      </radialGradient>
    </defs>
    <path d="M476 1110 Q600 1090 715 1090 Q830 1090 954 1110 Q900 1140 810 1150 Q760 1190 715 1190 Q670 1190 620 1150 Q530 1140 476 1110 Z" fill="url(#garland-petals)" opacity="0.75"/>
  </svg>

</main>
</body>
</html>
```